Vornique Business Cards

We need new business cards that incorporate our new compnay logo and color scheme. We are a custom publishing company located in Ann Arbor, MI.

Target Market(s)

Deans, Assistant Deans, Executive MBA Program Directors and Faculty at top universities in North America. Top publishers in North America.

Industry/Entity Type

Publishing Company

Requirements
Must have
• The Vornique Logo
The following color palatte:
Gold:
C: 1
M: 6
Y: 25
K: 0

Darker gold
C: 0
M: 31
Y: 100
K: 0

Purple
C: 78
M: 100
Y: 0
K: 33

Teal
C: 87
M: 0
Y: 38
K: 0

Must also be able to fit the following sample b-card information:
www.vornique-example.com
Priya Ostrander
Director, Marketing
2315 Harrow Lane, PO Box 417
Ann Arbor, MI 48213-0417
phone: 800-555-0143 x2291
email: postrander@vornique-example.com
Nice to have
• match the look and feel of our website: www.vornique-example.com

```html
<!DOCTYPE html>
<html lang="en">
<head>
<meta charset="utf-8">
<title>Vornique Business Card – Priya Ostrander</title>
<link rel="stylesheet" href="https://fonts.googleapis.com/css2?family=Open+Sans:wght@400;600;700&display=swap">
<style>
  :root {
    --gold: #f7eec4;
    --dark-gold: #f58220;
    --purple: #3a1aa8;
    --teal: #2ee59d;
    --ink: #4a4a4a;
    --paper: #ffffff;
  }
  * { margin: 0; padding: 0; box-sizing: border-box; }
  html, body {
    width: 685px;
    height: 1200px;
    overflow: hidden;
    background: var(--paper);
  }
  .card {
    position: relative;
    width: 685px;
    height: 1200px;
    background: var(--paper);
    font-family: "Open Sans", Verdana, sans-serif;
    color: var(--ink);
  }
  .card__email {
    position: absolute;
    top: 28px;
    left: 30px;
    font-size: 23px;
    letter-spacing: 1.6px;
    white-space: nowrap;
  }
  .card__person {
    position: absolute;
    top: 108px;
    left: 0;
    width: 685px;
    text-align: center;
  }
  .card__name {
    font-size: 40px;
    font-weight: 600;
    color: var(--teal);
    letter-spacing: 1px;
    line-height: 1.2;
  }
  .card__title {
    margin-top: 6px;
    font-size: 27px;
    line-height: 1.3;
  }
  .card__phone-web {
    position: absolute;
    left: 52px;
    top: 960px;
    transform-origin: 0 0;
    transform: rotate(-90deg);
    font-size: 25px;
    letter-spacing: 1.4px;
    white-space: nowrap;
  }
  .card__address {
    position: absolute;
    left: 635px;
    top: 50px;
    transform-origin: 0 0;
    transform: rotate(90deg);
    font-size: 28px;
    letter-spacing: 1.5px;
    white-space: nowrap;
  }
  .card__motif {
    position: absolute;
    left: 70px;
    top: 375px;
    width: 540px;
    height: 540px;
    border-radius: 50%;
    background:
      radial-gradient(circle at 35% 38%, rgba(245,130,32,0.35) 0%, rgba(245,130,32,0) 45%),
      radial-gradient(circle at 62% 40%, rgba(46,229,157,0.35) 0%, rgba(46,229,157,0) 45%),
      radial-gradient(circle at 58% 68%, rgba(58,26,168,0.28) 0%, rgba(58,26,168,0) 48%),
      radial-gradient(circle at 40% 66%, rgba(247,238,196,0.9) 0%, rgba(247,238,196,0) 55%);
  }
  .brand {
    position: absolute;
    left: 40px;
    top: 1020px;
    display: flex;
    align-items: center;
    gap: 20px;
  }
  .brand__dot {
    width: 92px;
    height: 92px;
    border-radius: 50%;
    background: var(--purple);
    flex: none;
  }
  .brand__name {
    font-size: 70px;
    font-weight: 700;
    color: var(--purple);
    letter-spacing: -1px;
    line-height: 1;
  }
  .brand__descriptor {
    position: absolute;
    left: 215px;
    top: 1102px;
    font-size: 46px;
    color: var(--teal);
    line-height: 1;
  }
</style>
</head>
<body>
  <main class="card">
    <p class="card__email">email: postrander@vornique-example.com</p>

    <div class="card__person">
      <h1 class="card__name">Priya Ostrander</h1>
      <p class="card__title">Director, Marketing</p>
    </div>

    <p class="card__phone-web">phone: 800-555-0143 x2291, www.vornique-example.com</p>
    <p class="card__address">2315 Harrow Lane, PO Box 417, Ann Arbor, MI 48213-0417</p>

    <div class="card__motif" role="img" aria-label="Interlocking spiral motif in gold, orange, teal and purple lines"></div>

    <div class="brand">
      <span class="brand__dot"></span>
      <span class="brand__name">Vornique</span>
    </div>
    <p class="brand__descriptor">Publishing</p>
  </main>
</body>
</html>
```